Civic Counsel and Advocacy Network needs poster design for landlord/tenant cases

We're seeking a poster design (11x17) to spread awareness for services by "Civic Counsel and Advocacy Network". The services they're trying to communicate are regarding housing/landlord/tenant matters.

We'd like the poster to (1) reflect the color scheme and branding of their website www.ccanmorvale.org, (2) contain the following copy: "Everyone needs safe and suitable housing, whether they own a home or rent one. When homelessness threatens, we at CCN help clients free of charge through eviction diversion programs and mortgage/tax foreclosure prevention.", and (3) contain their contact information:

Civic Counsel and Advocacy Network, Inc.
"We are YOUR Law Firm for Housing matters"
Contact us at: (555) 314-2869
housing @ccanmorvale.org
www.ccanmorvale.org

Target Market(s)

People who may be facing eviction or homelessness

Industry/Entity Type

Legal

Colors
0054AA
0677BA
7BADD7
CADEEF
E8F1F8
FFC000
F8CF3A
FAE287
FDF2CF
FEFAEE
EB3D1F
EC4F4E
F09395
F8D3D4
FCEDEE

Requirements
Must have
• Must include colors from website: https://ccanmorvale.org/

```html
<!DOCTYPE html>
<html lang="en">
<head>
<meta charset="utf-8">
<title>Civic Counsel and Advocacy Network – Housing Poster</title>
<link href="https://fonts.googleapis.com/css2?family=Tinos:wght@700&family=Source+Sans+3:wght@400;600&family=Libre+Baskerville:wght@400&display=swap" rel="stylesheet">
<style>
  :root{
    --navy:#243c8e;
    --navy-deep:#1d3a86;
    --footer:#2c4589;
    --red:#e2472f;
    --gold:#ab9457;
    --gold-dark:#8a7540;
    --ink:#1b1b1b;
    --white:#ffffff;
    --paper:#f4f4f5;
  }
  *{margin:0;padding:0;box-sizing:border-box}
  html,body{width:897px;height:1200px;overflow:hidden;background:var(--white)}
  .poster{position:relative;width:897px;height:1200px;overflow:hidden;
    background:radial-gradient(ellipse at 40% 78%,#ffffff 0%,#f3f3f4 55%,#e9e9eb 100%);
    font-family:"Source Sans 3",sans-serif}
  .hero{position:absolute;left:0;top:0;width:897px;height:600px}
  .wave{position:absolute;left:0;top:480px;width:897px;height:140px}
  .brand-tab{position:absolute;left:36px;top:0;width:445px;height:180px}
  .brand-mark{position:absolute;left:64px;top:49px;width:80px;height:80px;border-radius:50%;background:var(--navy-deep)}
  .brand-name{position:absolute;left:158px;top:58px;width:300px;color:var(--navy-deep);
    font-family:"Libre Baskerville",serif;font-weight:400;line-height:1}
  .brand-name .l1{display:block;font-size:16.5px;letter-spacing:.2px}
  .brand-name .l2{display:block;font-size:11px;letter-spacing:1.6px;margin-top:5px;padding-bottom:5px;border-bottom:1.5px solid var(--navy-deep)}
  .headline{position:absolute;left:42px;top:206px;font-family:"Tinos",serif;font-weight:700;
    font-size:49px;line-height:56px;color:var(--navy);letter-spacing:.3px}
  .headline .accent{color:var(--red)}
  .lead{position:absolute;left:41px;top:650px;font-size:27.5px;line-height:34px;color:var(--navy);font-weight:400}
  .rule{position:absolute;left:45px;top:789px;width:197px;height:4px;background:var(--gold)}
  .body-copy{position:absolute;left:45px;top:826px;width:366px;font-size:19.5px;line-height:26px;color:var(--ink)}
  .body-copy span{display:block;text-align:justify;text-align-last:justify}
  .body-copy span.last{text-align-last:left}
  .photo{position:absolute;background:var(--white);padding:7px;box-shadow:2px 4px 10px rgba(0,0,0,.28)}
  .photo div{width:100%;height:100%}
  .p-interior{left:474px;top:651px;width:215px;height:161px;transform:rotate(-4deg)}
  .p-interior div{background:linear-gradient(135deg,#d9d3cc,#8d8780 60%,#b9b3ac)}
  .p-houses{left:645px;top:674px;width:238px;height:166px;transform:rotate(3deg)}
  .p-houses div{background:linear-gradient(180deg,#dfe8f1 0%,#c98a62 45%,#8c9a6a 80%,#d9d6cf)}
  .p-family{left:678px;top:836px;width:215px;height:161px;transform:rotate(10deg)}
  .p-family div{background:linear-gradient(135deg,#e9edf2,#c2ccd9 50%,#d8c1ae)}
  .p-keys{left:442px;top:819px;width:249px;height:166px;transform:rotate(-8deg)}
  .p-keys div{background:linear-gradient(135deg,#f1f2f4,#d9c3b1 50%,#b7c3d6)}
  .footer{position:absolute;left:0;top:1087px;width:897px;height:113px;background:var(--footer)}
  .ribbon-fold{position:absolute;top:1046px;width:0;height:0}
  .ribbon-fold.left{left:9px;border-right:27px solid var(--gold-dark);border-top:42px solid transparent}
  .ribbon-fold.right{left:504px;border-left:27px solid var(--gold-dark);border-top:42px solid transparent}
  .ribbon{position:absolute;left:36px;top:1046px;width:468px;height:67px;background:var(--gold);
    color:var(--white);font-size:21.5px;line-height:67px;padding-left:25px;box-shadow:0 2px 4px rgba(0,0,0,.2)}
  .contact{position:absolute;top:1143px;display:flex;align-items:center;gap:6px;color:var(--white);font-size:19px;font-weight:600}
  .contact svg{width:17px;height:17px}
  .c-email{left:38px}.c-phone{left:395px}.c-web{left:634px}
</style>
</head>
<body>
<main class="poster">
  <svg class="hero" viewBox="0 0 897 600" role="img" aria-label="Bronze statue of blindfolded Lady Justice holding scales, on a warm tan background">
    <defs>
      <linearGradient id="heroBg" x1="0" y1="0" x2="1" y2="0.3">
        <stop offset="0" stop-color="#b9a283"/>
        <stop offset="0.35" stop-color="#eadfcf"/>
        <stop offset="0.6" stop-color="#f7f1e8"/>
        <stop offset="1" stop-color="#dcdfe6"/>
      </linearGradient>
      <radialGradient id="statue" cx="0.75" cy="0.45" r="0.4">
        <stop offset="0" stop-color="#5b554c"/>
        <stop offset="0.7" stop-color="#3a3835" stop-opacity=".8"/>
        <stop offset="1" stop-color="#3a3835" stop-opacity="0"/>
      </radialGradient>
    </defs>
    <rect width="897" height="600" fill="url(#heroBg)"/>
    <rect x="420" y="0" width="477" height="600" fill="url(#statue)"/>
  </svg>

  <svg class="wave" viewBox="0 480 897 140" preserveAspectRatio="none">
    <path d="M0 560 C120 520 200 512 290 517 C430 525 560 590 690 592 C800 594 860 560 897 505 L897 620 L0 620 Z" fill="var(--navy-deep)"/>
    <path d="M0 584 C120 545 200 535 290 538 C430 545 560 598 690 598 C800 598 860 575 897 530 L897 620 L0 620 Z" fill="#ffffff"/>
  </svg>

  <svg class="brand-tab" viewBox="0 0 445 180">
    <path d="M0 0 H445 V165 L225 180 L0 165 Z" fill="#ffffff"/>
  </svg>
  <div class="brand-mark"></div>
  <div class="brand-name">
    <span class="l1">CIVIC COUNSEL AND ADVOCACY</span>
    <span class="l2">NETWORK INCORPORATED</span>
  </div>

  <h1 class="headline">WE ARE YOUR<br><span class="accent">LAW FIRM</span><br>FOR HOUSING<br>MATTERS</h1>

  <p class="lead">Everyone needs safe and<br>suitable housing, whether<br>they own a home or rent one.</p>
  <div class="rule"></div>
  <p class="body-copy">
    <span>When homelessness threatens, we</span>
    <span>at CCN help clients free of charge</span>
    <span>through eviction diversion pro-</span>
    <span>grams and mortgage/tax foreclo-</span>
    <span class="last">sure prevention.</span>
  </p>

  <figure class="photo p-interior"><div role="img" aria-label="Bright dining room interior"></div></figure>
  <figure class="photo p-houses"><div role="img" aria-label="Row of suburban houses with red roofs"></div></figure>
  <figure class="photo p-family"><div role="img" aria-label="Family sitting together in a new home"></div></figure>
  <figure class="photo p-keys"><div role="img" aria-label="Hands holding house keys and a small model house"></div></figure>

  <div class="footer"></div>
  <div class="ribbon-fold left"></div>
  <div class="ribbon-fold right"></div>
  <div class="ribbon">Civic Counsel and Advocacy Network, Inc.</div>

  <div class="contact c-email">
    <svg viewBox="0 0 20 20"><circle cx="10" cy="10" r="9" fill="none" stroke="#fff" stroke-width="1.6"/><rect x="5" y="6.5" width="10" height="7" fill="none" stroke="#fff" stroke-width="1.4"/><path d="M5 6.5 L10 10.5 L15 6.5" fill="none" stroke="#fff" stroke-width="1.4"/></svg>
    housing @ccanmorvale.org
  </div>
  <div class="contact c-phone">
    <svg viewBox="0 0 20 20"><circle cx="10" cy="10" r="9" fill="none" stroke="#fff" stroke-width="1.6"/><path d="M7 5.5 L8.6 8 L7.6 9.2 C8.3 10.7 9.3 11.7 10.8 12.4 L12 11.4 L14.5 13 L13.5 14.6 C9.5 14.6 5.4 10.5 5.4 6.5 Z" fill="#fff"/></svg>
    (555) 314-2869
  </div>
  <div class="contact c-web">
    <svg viewBox="0 0 20 20"><g fill="none" stroke="#fff" stroke-width="1.4"><circle cx="10" cy="10" r="9"/><ellipse cx="10" cy="10" rx="4" ry="9"/><path d="M1 10 H19 M2.5 5.5 H17.5 M2.5 14.5 H17.5"/></g></svg>
    www.ccanmorvale.org
  </div>
</main>
</body>
</html>
```